BRIGHTDESK COWORKING Website design and coding

BRIGHTDESK COWORKING

BRIGHTDESK is Galveston’s first (and currently only) shared business co-working space. We share the same upscale, casual work environment, but we work independently on our own (or our team’s) projects and goals. For only a flat $195 membership fee per month, you have your very own all-inclusive, fun, personal business office environment. Website is written (Word file #12, below); and all pictures etc provided. Galveston is a beachy, coastal, historic city an hour from Houston, Texas USA. Logo (file 11 below) is temporary only.

Target Market(s)

Outside sales people, medical students looking for study hall, Houston companies looking for local office, real estate agents, graphic artists, entrepreneurs, etc

Contact Information for Business Card

will discuss --want to combine with current business card with multiple businesses

Logo Text

BRIGHTDESK COWORKING

Coding

Coded - Design and coding required

Number of Pages Required

5+ page

Colors
ec1f27
fbed22

Requirements
Nice to have
• maroon/wine dominant with yellow and red accents, gray base are the colors of the space--website could coordinate--but open to creative ideas/combinations

```html
<!DOCTYPE html>
<html lang="en">
<head>
<meta charset="utf-8">
<title>Brightdesk Coworking</title>
<link rel="stylesheet" href="https://fonts.googleapis.com/css2?family=Poppins:ital,wght@0,400;0,500;0,600;0,700;0,800;1,400;1,500;1,600;1,800&display=swap">
<style>
:root{
  --red:#ec1f27;
  --ink:#1d1d1f;
  --muted:#6b6b70;
  --line:#e6e6e9;
  --paper:#ffffff;
  --pink:#f9d4d8;
  --pink-frame:#f4b9c0;
  --hero-dark:#1f1a12;
  --hero-warm:#7a5a22;
}
*{box-sizing:border-box;margin:0;padding:0}
html,body{width:1200px;height:831px;overflow:hidden}
body{font-family:'Poppins',sans-serif;background:var(--paper);color:var(--ink);position:relative}

.topbar{height:30px;background:var(--red);display:flex;align-items:center;padding:0 40px;color:#fff;font-size:11px;gap:28px}
.topbar .item{display:flex;align-items:center;gap:7px}
.topbar .social{margin-left:auto;display:flex;gap:8px}
.topbar .social span{width:14px;height:14px;border-radius:50%;border:1.5px solid #fff;display:block}

.site-header{height:62px;display:flex;align-items:center;padding:0 40px;border-bottom:1px solid var(--line)}
.brand{display:flex;align-items:center;gap:9px;font-weight:600;font-size:19px;color:var(--ink)}
.brand .mark{width:26px;height:26px;background:var(--red)}
.main-nav{display:flex;gap:34px;margin-left:auto;margin-right:34px;font-size:11px;font-weight:500;text-transform:uppercase;letter-spacing:.4px}
.main-nav a{color:var(--ink);text-decoration:none}
.main-nav a.active{color:var(--red)}
.btn{display:inline-block;background:var(--red);color:#fff;font-size:11px;font-weight:500;text-transform:uppercase;letter-spacing:.5px;padding:11px 20px;border-radius:4px;text-decoration:none;line-height:1.4}

.hero{position:relative;height:300px;display:flex;flex-direction:column;align-items:center;justify-content:center;text-align:center;color:#fff}
.hero-photo{position:absolute;inset:0;background:radial-gradient(ellipse at 60% 70%,var(--hero-warm) 0%,#4a3818 40%,var(--hero-dark) 85%)}
.hero-content{position:relative}
.hero .eyebrow{font-size:13px;letter-spacing:1.5px;text-transform:uppercase;margin-bottom:8px}
.hero h1{font-size:38px;font-weight:800;font-style:italic;line-height:1.22;margin-bottom:20px}
.hero .arrow{position:absolute;top:50%;width:28px;height:28px;margin-top:-14px;border-radius:50%;display:flex;align-items:center;justify-content:center}
.hero .arrow.prev{left:22px;background:#fff}
.hero .arrow.next{right:22px;background:var(--red)}

.about{display:flex;padding:18px 40px 0;height:228px;gap:40px;overflow:hidden}
.about-gallery{position:relative;width:520px;height:196px;flex:none}
.about-gallery .frame{position:absolute;left:0;top:10px;width:250px;height:180px;border:4px solid var(--pink-frame)}
.about-gallery .shot{position:absolute;border:4px solid #fff;box-shadow:0 4px 12px rgba(0,0,0,.18)}
.about-gallery .shot.one{left:20px;top:0;width:260px;height:150px;background:linear-gradient(135deg,#c9a98a,#6e5a48)}
.about-gallery .shot.two{left:230px;top:50px;width:280px;height:146px;background:linear-gradient(135deg,#9fb3c4,#4e4a42)}
.about-text{flex:1}
.section-label{color:var(--red);font-size:19px;font-weight:600;line-height:1.5;margin-bottom:2px}
.about-text .lead{font-size:12px;line-height:1.5;margin-bottom:8px}
.features{display:flex;gap:26px;margin-bottom:8px}
.feature{display:flex;gap:9px}
.feature h3{font-size:12px;font-weight:600;line-height:1.4;margin-bottom:1px}
.feature p{font-size:9.5px;color:var(--muted);line-height:1.45}
.about-text .body{font-size:12px;line-height:1.5;margin-bottom:8px}
.btn.pill{border-radius:20px;text-transform:none;padding:7px 22px}

.amenities{text-align:center;padding-top:4px}
.amenities h2{color:var(--red);font-size:18px;font-weight:600;line-height:1.5;text-transform:uppercase;font-style:italic}
.amenities .intro{font-size:10px;color:var(--muted);margin:2px auto 8px;max-width:520px;line-height:1.45}
.cards{display:flex;justify-content:center;gap:26px}
.card{width:250px;height:130px;background:var(--paper);border:1px solid var(--line);border-radius:6px;box-shadow:0 3px 10px rgba(0,0,0,.06);padding:8px 18px;display:flex;flex-direction:column;align-items:center}
.card.highlight{background:var(--pink)}
.card .icon{width:28px;height:28px;border-radius:50%;background:#fff;display:flex;align-items:center;justify-content:center;box-shadow:0 1px 4px rgba(0,0,0,.12);flex:none}
.card.highlight .icon{background:var(--red)}
.card h3{font-size:14px;font-weight:500;line-height:1.4;margin:4px 0 2px}
.card p{font-size:9.5px;line-height:1.4;color:var(--muted)}
.card a{font-size:10px;font-style:italic;font-weight:600;color:var(--red);text-decoration:none;margin-top:3px}
.card.highlight a{color:var(--ink)}
</style>
</head>
<body>

<div class="topbar">
  <div class="item">
    <svg width="12" height="12" viewBox="0 0 24 24" fill="#fff"><path d="M6.6 10.8a15.1 15.1 0 0 0 6.6 6.6l2.2-2.2c.3-.3.7-.4 1-.2 1.1.4 2.3.6 3.6.6.6 0 1 .4 1 1V20c0 .6-.4 1-1 1C10.6 21 3 13.4 3 4c0-.6.4-1 1-1h3.5c.6 0 1 .4 1 1 0 1.3.2 2.5.6 3.6.1.3 0 .7-.2 1z"/></svg>
    <span>409-555-0142</span>
  </div>
  <div class="item">
    <svg width="13" height="11" viewBox="0 0 24 18" fill="none" stroke="#fff" stroke-width="2"><rect x="1" y="1" width="22" height="16" rx="2"/><path d="M1 2l11 8 11-8"/></svg>
    <span>hello@brightdesk-demo.com</span>
  </div>
  <div class="social"><span></span><span></span><span></span></div>
</div>

<header class="site-header">
  <div class="brand"><span class="mark"></span>Brightdesk Coworking</div>
  <nav class="main-nav">
    <a class="active" href="#">Home</a>
    <a href="#">About us</a>
    <a href="#">Pictures</a>
    <a href="#">Amenities</a>
    <a href="#">Membership</a>
    <a href="#">Contact us</a>
  </nav>
  <a class="btn" href="#">Schedule a tour</a>
</header>

<section class="hero">
  <div class="hero-photo" role="img" aria-label="Coworking meeting room with long wooden table and pendant lamps"></div>
  <div class="hero-content">
    <p class="eyebrow">The best workspace in Texas</p>
    <h1>Professionals, Creative,<br>Flexible, Scalalble Workspace</h1>
    <a class="btn" href="#">Book a tour</a>
  </div>
  <span class="arrow prev"><svg width="12" height="12" viewBox="0 0 24 24" fill="none" stroke="#ec1f27" stroke-width="3"><path d="M20 12H5M11 5l-7 7 7 7"/></svg></span>
  <span class="arrow next"><svg width="12" height="12" viewBox="0 0 24 24" fill="none" stroke="#fff" stroke-width="3"><path d="M4 12h15M13 5l7 7-7 7"/></svg></span>
</section>

<section class="about">
  <div class="about-gallery">
    <div class="frame"></div>
    <div class="shot one" role="img" aria-label="Lounge area with copper pendant lamps"></div>
    <div class="shot two" role="img" aria-label="Open work area with desks and yellow chairs"></div>
  </div>
  <div class="about-text">
    <h2 class="section-label">About us</h2>
    <p class="lead">BRIGHTDESK is Galveston’s first (and currently only) shared business co-working space.We share the same upscale</p>
    <div class="features">
      <div class="feature">
        <svg width="22" height="22" viewBox="0 0 24 24" fill="none" stroke="#ec1f27" stroke-width="1.8"><path d="M2 12l4-4 4 2 4-2 4 2 4 2M6 14l3 3 2-1 2 2 2-1 3-3"/></svg>
        <div><h3>Trusted by Thousands</h3><p>Lorem ipsum dolor sit amet,<br>consetetur sadipscing elitr,<br>sed diam nonumy eirmod</p></div>
      </div>
      <div class="feature">
        <svg width="22" height="22" viewBox="0 0 24 24" fill="none" stroke="#ec1f27" stroke-width="1.8"><rect x="3" y="4" width="18" height="16" rx="1"/><path d="M3 9h18M8 13h3M13 13h3M8 16h3M13 16h3"/></svg>
        <div><h3>Workspace Solutions</h3><p>Lorem ipsum dolor sit amet,<br>consetetur sadipscing elitr,<br>sed diam nonumy eirmod</p></div>
      </div>
    </div>
    <p class="body">Lorem ipsum dolor sit amet, consetetur sadipscing elitr, sed diam nonumy eirmod</p>
    <a class="btn pill" href="#">Read more</a>
  </div>
</section>

<section class="amenities">
  <h2>Our amenities</h2>
  <p class="intro">BRIGHTDESK is the first Galveston co-working space, and offers all of the following features, all included in your monthly $195 membership fee</p>
  <div class="cards">
    <div class="card highlight">
      <span class="icon"><svg width="14" height="14" viewBox="0 0 24 24" fill="none" stroke="#fff" stroke-width="2"><rect x="6" y="2" width="12" height="20" rx="1"/><circle cx="15" cy="12" r="1" fill="#fff"/></svg></span>
      <h3>Daily open</h3>
      <p>Lorem ipsum dolor sit amet, consetetur sadipscing elitr, sed diam nonumy eirmod tempor invidunt.</p>
      <a href="#">Learn More</a>
    </div>
    <div class="card">
      <span class="icon"><svg width="15" height="15" viewBox="0 0 24 24" fill="none" stroke="#ec1f27" stroke-width="2"><path d="M2 9a15 15 0 0 1 20 0M5 13a10 10 0 0 1 14 0M8.5 16.5a5 5 0 0 1 7 0"/><circle cx="12" cy="20" r="1.2" fill="#ec1f27"/></svg></span>
      <h3>Free wifi</h3>
      <p>Lorem ipsum dolor sit amet, consetetur sadipscing elitr, sed diam nonumy eirmod tempor invidunt.</p>
      <a href="#">Learn More</a>
    </div>
    <div class="card">
      <span class="icon"><svg width="15" height="15" viewBox="0 0 24 24" fill="none" stroke="#ec1f27" stroke-width="2"><circle cx="12" cy="12" r="9"/><path d="M12 7v5l3 2"/></svg></span>
      <h3>24 Hour</h3>
      <p>Lorem ipsum dolor sit amet, consetetur sadipscing elitr, sed diam nonumy eirmod tempor invidunt.</p>
      <a href="#">Learn More</a>
    </div>
  </div>
</section>

</body>
</html>
```